Design Business Card MAPLE WREN MOWING

We have attached a copy of our Logo, we like a business card designed with logo and mobile phone number on one side that stands out maybe gloss and on the other side it can have the services we do small picture of our logo name number, I have attached an idea to this that I have seen online, this is a business owned by a woman so we like pinks black and navy
Our logo is attached in pdf
Target Market(s)
Home owners that need lawns mowed
Industry/Entity Type
Lawns and gardens
Contact Information for Business Card
Logo business Owner name Deborah Finch mobile number 0491627504
Font styles to use
Look and feel
Each slider illustrates characteristics of the customer's brand and the style your logo design should communicate.

```html
<!DOCTYPE html>
<html lang="en">
<head>
<meta charset="UTF-8">
<title>Maple Wren Mowing – Business Card</title>
<link rel="stylesheet" href="https://fonts.googleapis.com/css2?family=Teko:wght@500;600&display=swap">
<style>
  :root {
    --stage: #2c2e30;
    --pink-light: #ea6fb0;
    --pink: #d53d8f;
    --pink-deep: #c2247a;
    --ink: #1c1a1b;
    --black: #0a0a0a;
    --white: #ffffff;
    --green: #3fbf4a;
  }
  * { margin: 0; padding: 0; box-sizing: border-box; }
  html, body {
    width: 1200px;
    height: 939px;
    overflow: hidden;
    background: var(--stage);
    font-family: "Teko", "Arial Narrow", sans-serif;
  }
  .card {
    position: absolute;
    width: 560px;
    height: 320px;
    border-radius: 4px;
    box-shadow: 0 18px 40px rgba(0,0,0,0.45);
    display: flex;
    flex-direction: column;
    align-items: center;
    justify-content: center;
    text-align: center;
  }
  .card-front {
    left: 80px;
    top: 90px;
    background: radial-gradient(ellipse at 50% 45%, var(--pink-light) 0%, var(--pink) 55%, var(--pink-deep) 100%);
    color: var(--ink);
  }
  .card-back {
    left: 560px;
    top: 520px;
    background: var(--black);
    color: var(--white);
  }
  .brand {
    display: flex;
    align-items: center;
    gap: 14px;
  }
  .brand-dot {
    width: 34px;
    height: 34px;
    border-radius: 50%;
  }
  .brand-name {
    font-weight: 600;
    letter-spacing: 1px;
    line-height: 1;
  }
  .card-front .brand-dot { background: var(--ink); }
  .card-front .brand-name { font-size: 50px; color: var(--ink); }
  .front-call {
    margin-top: 34px;
    font-size: 30px;
    font-weight: 600;
    letter-spacing: 2px;
    color: var(--ink);
  }
  .card-back .brand-dot { background: var(--pink); width: 26px; height: 26px; }
  .card-back .brand-name { font-size: 38px; color: var(--pink); }
  .services {
    margin-top: 18px;
    font-size: 19px;
    font-weight: 600;
    letter-spacing: 1px;
    line-height: 1.05;
  }
  .services .sep { color: var(--pink); padding: 0 4px; }
  .owner-name {
    margin-top: 12px;
    font-size: 36px;
    font-weight: 600;
    letter-spacing: 2px;
    color: var(--pink);
    line-height: 1;
  }
  .owner-role {
    font-size: 17px;
    font-weight: 600;
    letter-spacing: 1px;
    line-height: 1.1;
  }
  .owner-phone {
    margin-top: 6px;
    display: flex;
    align-items: center;
    gap: 8px;
    font-size: 24px;
    font-weight: 600;
    letter-spacing: 2px;
  }
  .owner-phone svg { width: 20px; height: 20px; }
</style>
</head>
<body>
  <section class="card card-front">
    <div class="brand">
      <span class="brand-dot"></span>
      <span class="brand-name">MAPLE WREN MOWING</span>
    </div>
    <p class="front-call">CALL: 0491627504</p>
  </section>

  <section class="card card-back">
    <div class="brand">
      <span class="brand-dot"></span>
      <span class="brand-name">MAPLE WREN MOWING</span>
    </div>
    <p class="services">
      GARDEN MAINTENANCE<span class="sep">|</span>RUBBISH REMOVAL<span class="sep">|</span>TRIMMING<br>
      WEEDING<span class="sep">|</span>LAWN CARE
    </p>
    <p class="owner-name">DEBORAH FINCH</p>
    <p class="owner-role">OWNER</p>
    <p class="owner-phone">
      <svg viewBox="0 0 24 24" aria-hidden="true">
        <path fill="var(--green)" d="M6.6 10.8a15.1 15.1 0 0 0 6.6 6.6l2.2-2.2a1 1 0 0 1 1-.25 11.4 11.4 0 0 0 3.6.57 1 1 0 0 1 1 1V20a1 1 0 0 1-1 1A17 17 0 0 1 3 4a1 1 0 0 1 1-1h3.5a1 1 0 0 1 1 1c0 1.25.2 2.45.57 3.57a1 1 0 0 1-.25 1z"/>
      </svg>
      0491627504
    </p>
  </section>
</body>
</html>
```